Web design/Online store for an online apparel company

We need a website designed for an online apparel company called Kestrel Lantern Co. We need the categories for T-shirts, Tanks, Hoodies, and Headwear. Under T-shirts, we need the sub-categories of City/State Edition, Legendary Quotes, Logo, Nature, American, Christian, and Heritage Edition. We have a simple logo using the colors black, white, and gray/silver. We'd like the website to match. When using an accent color, use a shade of blue. The purpose of our company is to make apparel for people that is affordable, comfortable for any almost any occasion, and meaningful to the person wearing the clothing. Logo uploaded below.

```html
<!DOCTYPE html>
<html lang="en">
<head>
<meta charset="utf-8">
<title>Kestrel Lantern Co — Online Apparel Store</title>
<link href="https://fonts.googleapis.com/css2?family=Arvo:wght@400;700&family=Lora:wght@400;600&display=swap" rel="stylesheet">
<style>
:root{
  --black:#000;
  --ink:#0b0b0b;
  --panel:#1d1d1d;
  --footer:#161616;
  --white:#fff;
  --grey:#bdbdbd;
  --muted:#9a9a9a;
  --silver-a:#f2f2f2;
  --silver-b:#8e8e8e;
  --blue:#1487d4;
  --star:#f4b400;
  --line:#3a3a3a;
}
*{box-sizing:border-box;margin:0;padding:0}
html,body{width:1200px;height:5155px;overflow:hidden;background:var(--black)}
body{position:relative;font-family:'Lora',Georgia,serif;color:var(--white)}
.abs{position:absolute}
.heading{font-family:'Arvo',Georgia,serif;font-weight:400;letter-spacing:3px;text-transform:uppercase}
.btn{position:absolute;display:flex;align-items:center;justify-content:center;font-family:'Arvo',serif;font-size:15px;font-weight:700;letter-spacing:1px;color:#111;background:linear-gradient(90deg,#f4f4f4,#9a9a9a);}
.btn.blue{background:var(--blue);color:var(--white)}
.rule{position:absolute;height:2px;background:linear-gradient(90deg,transparent,var(--grey),transparent)}
.photo{position:absolute}

/* header */
.search{left:104px;top:24px;width:352px;height:38px;border:1px solid #777;display:flex;align-items:center;padding-left:14px;font-size:12px;gap:10px}
.nav a{position:absolute;top:102px;font-family:'Arvo',serif;font-size:15px;color:var(--white);text-decoration:none}
.nav a.active{color:var(--blue)}
.brand{left:520px;top:40px;width:160px;text-align:center;font-family:'Arvo',serif;font-size:15px;letter-spacing:2px;line-height:1.4;display:flex;flex-direction:column;align-items:center;gap:8px}
.brand .mark{width:22px;height:22px;background:var(--grey)}
.user{top:30px;display:flex;align-items:center;gap:14px;font-family:'Arvo',serif;font-size:15px}
.user .ico{width:36px;height:36px;border:1px solid #888;transform:rotate(45deg);display:flex;align-items:center;justify-content:center}
.user .ico svg{transform:rotate(-45deg)}

/* hero */
.hero{left:0;top:155px;width:1200px;height:600px;background:linear-gradient(90deg,#1a1a1a,#0c0c0c 60%,#111)}
.hero .photo{left:0;top:0;width:620px;height:600px;background:radial-gradient(circle at 40% 40%,#6e6e60,#2a2a28 55%,#0d0d0d)}
.hero-text{left:640px;top:120px;width:460px}
.hero-text .eyebrow{font-size:22px;letter-spacing:1px}
.hero-text h1{font-size:58px;line-height:66px;margin:14px 0 20px;letter-spacing:4px}
.hero-text p{font-size:15px;line-height:28px;color:var(--grey)}
.dots span{position:absolute;left:1140px;width:12px;height:12px;transform:rotate(45deg);background:#666}
.dots span.on{background:var(--white)}

/* titles */
.sec-title{position:absolute;left:0;width:1200px;text-align:center;font-size:40px}

/* category cards */
.cat{position:absolute;width:496px;height:226px;border:2px solid #8c8c8c;overflow:hidden}
.cat .txt{position:absolute;left:28px;top:24px;width:260px}
.cat h3{font-family:'Arvo',serif;font-weight:400;font-size:27px;margin-bottom:12px}
.cat p{font-size:12px;line-height:23px}
.cat.light{background:linear-gradient(90deg,#cfcfcf,#f3f3f3);color:#111}
.cat.dark{background:linear-gradient(90deg,#3e3e3e,#9a9a9a)}
.cat.sand{background:linear-gradient(90deg,#585450,#8d8a85 60%,#a89f98)}
.cat.shore{background:linear-gradient(90deg,#5d6770,#9aa4aa 60%,#b6bcc0)}
.cat .photo{right:0;top:0;width:240px;height:226px}

/* featured */
.featured{left:0;top:1548px;width:1200px;height:696px;background:linear-gradient(90deg,#8a8a8a,#f4f4f4 30%,#fff 50%,#e8e8e8 70%,#8c8c8c)}
.prod{position:absolute;width:240px;height:390px;background:var(--black);border:3px solid #111;text-align:center}
.prod.active{border-color:var(--blue)}
.prod .photo{left:6px;top:6px;width:222px;height:218px}
.prod .name{position:absolute;left:0;right:0;top:240px;font-size:14px}
.prod .price{position:absolute;left:0;right:0;top:264px;font-size:19px;font-weight:600}
.prod .stars{position:absolute;left:0;right:0;top:294px;color:var(--star);font-size:13px;letter-spacing:1px}
.prod .btn{left:64px;top:326px;width:106px;height:32px;font-size:11px}
.prod .tools{position:absolute;right:14px;top:14px;display:flex;flex-direction:column;gap:10px}
.prod .tools span{width:22px;height:22px;background:#111;border:1px solid #fff;transform:rotate(45deg)}
.arrow{position:absolute;width:54px;height:54px;border-radius:50%;background:var(--black);border:2px solid #fff;display:flex;align-items:center;justify-content:center;font-family:'Arvo',serif;font-size:26px;color:#fff;line-height:1}

/* about */
.about-text{left:640px;top:2470px;width:420px}
.about-text h2{font-size:40px;margin-bottom:22px}
.about-text p{font-size:15px;line-height:26px;color:var(--grey);margin-bottom:14px}

/* custom */
.custom{left:0;top:2962px;width:1200px;height:582px;background:var(--panel)}
.custom-text{left:104px;top:170px;width:420px}
.custom-text h2{font-size:40px;line-height:58px;color:#d9d9d9;margin-bottom:18px}
.custom-text p{font-size:15px;line-height:26px;color:var(--grey)}

/* insta */
.tile{position:absolute;top:4402px;width:216px;height:216px}

/* footer */
.footer{left:0;top:4740px;width:1200px;height:415px;background:var(--footer)}
.footer-brand{left:104px;top:140px;width:200px;display:flex;flex-direction:column;align-items:center;gap:14px;text-align:center;font-family:'Arvo',serif;font-size:18px;line-height:26px;letter-spacing:2px}
.footer-brand .mark{width:24px;height:24px;background:var(--grey)}
.footer h4{position:absolute;top:88px;font-family:'Arvo',serif;font-weight:400;font-size:21px;letter-spacing:1px}
.footer ul{position:absolute;top:134px;list-style:none;font-size:14px;line-height:29px;color:#ddd}
.newsletter-input{left:746px;top:128px;width:352px;height:44px;border:1px solid #777;display:flex;align-items:center;gap:14px;padding-left:14px;font-size:13px}
.pay{position:absolute;top:250px;display:flex;gap:6px;left:746px}
.pay span{width:40px;height:24px;border-radius:3px}
</style>
</head>
<body>

<!-- header -->
<div class="abs search"><svg width="13" height="13" viewBox="0 0 14 14"><circle cx="6" cy="6" r="4.5" fill="none" stroke="#fff" stroke-width="2"/><line x1="9.5" y1="9.5" x2="13" y2="13" stroke="#fff" stroke-width="2"/></svg>Search Product......</div>
<div class="abs" style="left:104px;top:84px;width:396px;height:1px;background:#555"></div>
<div class="abs" style="left:700px;top:84px;width:396px;height:1px;background:#555"></div>
<nav class="nav">
  <a class="active" style="left:104px">Home</a>
  <a style="left:186px">About Us</a>
  <a style="left:296px">Category</a>
  <a style="left:406px">Products</a>
  <a style="left:700px">Testimonials</a>
  <a style="left:840px">Latest News</a>
  <a style="left:974px">Contact Us</a>
</nav>
<div class="abs brand"><span class="mark"></span>KESTREL<br>LANTERN CO</div>
<div class="abs user" style="left:858px"><span class="ico"><svg width="14" height="14" viewBox="0 0 14 14"><circle cx="7" cy="4.5" r="3" fill="#fff"/><path d="M1 13c0-4 12-4 12 0z" fill="#fff"/></svg></span>Log In</div>
<div class="abs user" style="left:988px"><span class="ico"><svg width="14" height="14" viewBox="0 0 14 14"><path d="M1 2h2l2 7h7l1-5H4" fill="none" stroke="#fff" stroke-width="1.5"/><circle cx="6" cy="12" r="1.2" fill="#fff"/><circle cx="11" cy="12" r="1.2" fill="#fff"/></svg></span><b>$0.00</b></div>

<!-- hero -->
<section class="abs hero">
  <div class="photo" role="img" aria-label="Model in a black logo t-shirt and brown trousers against a dark studio backdrop"></div>
  <div class="abs hero-text">
    <div class="eyebrow">Welcome To</div>
    <h1 class="heading">Kestrel<br>Lantern Co</h1>
    <p>Lorem ipsum dolor sit amet, consectetur adipiscing elit, sed do eiusmod dolore magna aliqua.</p>
  </div>
  <div class="btn" style="left:640px;top:431px;width:138px;height:40px">SHOP NOW</div>
  <div class="dots"><span class="on" style="top:248px"></span><span style="top:280px"></span><span style="top:312px"></span><span style="top:344px"></span></div>
</section>

<!-- categories -->
<div class="rule" style="left:560px;top:862px;width:80px"></div>
<h2 class="heading sec-title" style="top:896px">Product Categories</h2>

<div class="cat dark" style="left:94px;top:998px">
  <div class="photo" role="img" aria-label="Man in glasses wearing a black logo t-shirt"></div>
  <div class="txt"><h3>T-shirts</h3><p>City State Edition, Legendary Quotes, Logo, Nature, American, Christian, and Heritage Edition</p></div>
  <div class="btn blue" style="left:28px;top:148px;width:138px;height:40px">SHOP NOW</div>
</div>
<div class="cat light" style="left:610px;top:998px">
  <div class="photo" role="img" aria-label="Woman in a white tank top on a light background"></div>
  <div class="txt"><h3>Tanks</h3><p>Lorem ipsum dolor sit amet, adipiscing elit</p></div>
  <div class="btn" style="left:28px;top:148px;width:138px;height:40px">SHOP NOW</div>
</div>
<div class="cat sand" style="left:94px;top:1242px">
  <div class="photo" role="img" aria-label="Couple in green and red hoodies on a beach"></div>
  <div class="txt"><h3>Hoodies</h3><p>Lorem ipsum dolor sit amet, adipiscing elit</p></div>
  <div class="btn" style="left:28px;top:148px;width:138px;height:40px">SHOP NOW</div>
</div>
<div class="cat shore" style="left:610px;top:1242px">
  <div class="photo" role="img" aria-label="Two people wearing caps by the sea"></div>
  <div class="txt"><h3>Headwear</h3><p>Lorem ipsum dolor sit amet, adipiscing elit</p></div>
  <div class="btn" style="left:28px;top:148px;width:138px;height:40px">SHOP NOW</div>
</div>

<!-- featured -->
<section class="abs featured">
  <div class="rule" style="left:560px;top:106px;width:80px;background:linear-gradient(90deg,transparent,#333,transparent)"></div>
  <h2 class="heading sec-title" style="top:138px;color:#111">Featured Products</h2>
  <div class="prod" style="left:98px;top:228px"><div class="photo" role="img" aria-label="Man in a black long-sleeve t-shirt" style="background:linear-gradient(#cfcfcf,#9c9c9c)"></div><div class="name">T - Shirt</div><div class="price">$250.00</div><div class="stars">★★★★★</div><div class="btn">SHOP NOW</div></div>
  <div class="prod" style="left:354px;top:228px"><div class="photo" role="img" aria-label="Woman in a white tank top" style="background:linear-gradient(#e6e6e6,#bdbdbd)"></div><div class="name">Tanks</div><div class="price">$250.00</div><div class="stars">★★★★★</div><div class="btn">SHOP NOW</div></div>
  <div class="prod active" style="left:608px;top:228px"><div class="photo" role="img" aria-label="Young man in a white hoodie outdoors" style="background:linear-gradient(#6d7a84,#c9ccd0)"></div><div class="tools"><span></span><span></span></div><div class="name">Hoodies</div><div class="price">$250.00</div><div class="stars">★★★★★</div><div class="btn blue">SHOP NOW</div></div>
  <div class="prod" style="left:864px;top:228px"><div class="photo" role="img" aria-label="Man adjusting a black cap" style="background:linear-gradient(#5b6166,#23272a)"></div><div class="name">Headwear</div><div class="price">$250.00</div><div class="stars">★★★★★</div><div class="btn">SHOP NOW</div></div>
  <div class="arrow" style="left:19px;top:395px">«</div>
  <div class="arrow" style="left:1125px;top:395px">»</div>
</section>

<!-- about -->
<svg class="abs" style="left:70px;top:2370px" width="460" height="460" viewBox="0 0 460 460">
  <defs><linearGradient id="frame" x1="0" y1="0" x2="1" y2="1"><stop offset="0" stop-color="#f0f0f0"/><stop offset="1" stop-color="#777"/></linearGradient></defs>
  <polygon points="230,0 460,230 230,460 0,230" fill="url(#frame)"/>
  <polygon points="230,18 442,230 230,442 18,230" fill="#f2b80f" role="img" aria-label="Couple in black t-shirts against a yellow wall"/>
</svg>
<div class="rule" style="left:640px;top:2444px;width:60px"></div>
<div class="abs about-text">
  <h2 class="heading">About Us</h2>
  <p>Lorem ipsum dolor sit amet, consectetur adipiscing elit, sed do eiusmod tempor incididunt ut labore et dolore magna aliqua. Quis ipsum suspendisse ultrices gravida. Risus commodo viverra maecenas accumsan lacus vel facilisis.</p>
  <p>Sed ut perspiciatis unde omnis iste natus error sit voluptatem accusantium doloremque laudantium, totam rem vitae dicta sunt explicabo.</p>
</div>
<div class="btn" style="left:640px;top:2786px;width:140px;height:40px">READ MORE</div>

<!-- customized -->
<section class="abs custom">
  <div class="rule" style="left:104px;top:130px;width:60px"></div>
  <div class="abs custom-text">
    <h2 class="heading">Customized<br>T - Shirts</h2>
    <p>Lorem ipsum dolor sit amet, consectetur adipiscing elit, sed do eiusmod tempor incididunt ut labore et dolore magna aliqua. Quis ipsum suspendisse ultrices gravida. Risus commodo viverra maecenas accumsan lacus vel facilisis.</p>
  </div>
  <div class="btn" style="left:104px;top:440px;width:140px;height:40px">SHOP NOW</div>
  <div class="photo" role="img" aria-label="Hands folding a lavender t-shirt on a work table" style="left:600px;top:0;width:600px;height:582px;background:linear-gradient(160deg,#3a2a22,#5a4638 40%,#a486c8 70%,#d8cdbb)"></div>
</section>

<!-- subcategories -->
<div class="rule" style="left:560px;top:3660px;width:80px"></div>
<h2 class="heading sec-title" style="top:3710px">T-Shirt Subcategories</h2>
<div class="prod" style="left:96px;top:3796px;border-color:transparent"><div class="photo" role="img" aria-label="Man in a black city edition graphic tee" style="background:linear-gradient(#e0e0e0,#bcbcbc)"></div><div class="name">City/State Edition</div><div class="price">$250.00</div><div class="stars">★★★★★</div><div class="btn">SHOP NOW</div></div>
<div class="prod" style="left:352px;top:3796px;border-color:transparent"><div class="photo" role="img" aria-label="Man in a black quote graphic tee" style="background:linear-gradient(#3a3a3a,#111)"></div><div class="name">Legendary Quotes</div><div class="price">$250.00</div><div class="stars">★★★★★</div><div class="btn">SHOP NOW</div></div>
<div class="prod" style="left:606px;top:3796px;border-color:#777"><div class="photo" role="img" aria-label="Man in a black logo tee on a city street" style="background:linear-gradient(#6d6a66,#2d2b2a)"></div><div class="tools"><span></span><span></span></div><div class="name">Logo</div><div class="price">$250.00</div><div class="stars">★★★★★</div><div class="btn blue">SHOP NOW</div></div>
<div class="prod" style="left:862px;top:3796px;border-color:transparent"><div class="photo" role="img" aria-label="White nature graphic tee" style="background:radial-gradient(circle,#f4f4f4 45%,#000 46%)"></div><div class="name">Nature</div><div class="price">$250.00</div><div class="stars">★★★★★</div><div class="btn">SHOP NOW</div></div>
<div class="arrow" style="left:19px;top:3968px">«</div>
<div class="arrow" style="left:1125px;top:3968px">»</div>

<!-- follow -->
<div class="abs" style="left:104px;top:4268px;width:992px;height:1px;background:#777"></div>
<h2 class="heading sec-title" style="top:4318px;color:#ddd">Follow @ Kestrel Lantern Co</h2>
<div class="tile" role="img" aria-label="Woman in a white tee" style="left:34px;background:linear-gradient(#d9cfc6,#a57a52)"></div>
<div class="tile" role="img" aria-label="White graphic tee on an orange backdrop" style="left:264px;background:radial-gradient(circle,#f2f2f2 35%,#c9471f 36%)"></div>
<div class="tile" style="left:494px;background:#3a8fd0" role="img" aria-label="Man in a denim shirt with a blue overlay"><svg style="position:absolute;left:94px;top:94px" width="28" height="28" viewBox="0 0 28 28"><circle cx="14" cy="14" r="12" fill="none" stroke="#fff" stroke-width="2"/></svg></div>
<div class="tile" role="img" aria-label="Man in a black graphic hoodie" style="left:720px;background:linear-gradient(#eaeaea,#1a1a1a)"></div>
<div class="tile" role="img" aria-label="Woman in a blue cap" style="left:950px;background:linear-gradient(90deg,#3a3f44,#6c747b,#2b2f33)"></div>

<!-- footer -->
<footer class="abs footer">
  <div class="abs footer-brand"><span class="mark"></span><span>KESTREL<br>LANTERN CO</span></div>
  <h4 style="left:346px">Quick Links</h4>
  <ul style="left:346px"><li>Home</li><li>About Us</li><li>Category</li><li>Products</li><li>Testimonials</li><li>Latest News</li><li>Contact Us</li></ul>
  <h4 style="left:530px">Links</h4>
  <ul style="left:530px;line-height:32px"><li>FAQ</li><li>Size Guide</li><li>Shipping Policy</li><li>Return &amp; Refund Policy</li><li>Terms of Service</li><li>Privacy Policy</li></ul>
  <h4 style="left:746px">Newsletter</h4>
  <div class="abs newsletter-input"><svg width="16" height="12" viewBox="0 0 16 12"><rect width="16" height="12" fill="#fff"/><path d="M0 0l8 6 8-6" fill="none" stroke="#161616" stroke-width="1.5"/></svg>Enter Email</div>
  <div class="btn" style="left:746px;top:190px;width:110px;height:30px;font-size:11px">SUBMIT</div>
  <div class="pay"><span style="background:#c9c9c9"></span><span style="background:#e8e8e8"></span><span style="background:#d0d6e6"></span><span style="background:#f1f1f1"></span><span style="background:#4f87c4"></span><span style="background:#dedede"></span></div>
  <div class="abs" style="left:104px;top:330px;width:992px;height:1px;background:#555"></div>
  <div class="abs" style="left:0;top:364px;width:1200px;text-align:center;font-size:12px">Copyright © 2024 Kestrel Lantern Co | All rights reserved.</div>
</footer>

</body>
</html>
```